Legal Website Custom Template Design - Wordpress 3.0+

I need an original template designed in Wordpress (Wordpress 3.0+ compatible with widget support) for a legal website. The template should be designed so that 2 language versions of the same site can be supported at the same time (e.g., clicking on the language link on the upper right hand side will switch the content from English to another language). Also, the template should be flexible enough that I can add additional tabs, navigation as needed as part of the widgeting process.
The overall theme of my website should be to look simple, elegant, smart and professional.
I am envisioning 5 templates (see attached document for details of each tab and further project description).
6 tabs along the upper portion of the website, going left to right. There should be three different types of templates:
a. Home page (1st tab) that supports adds to the tabs on top for all pages.
b. Content page Level 1 (2nd tab (“Attorney/Staff Profiles”) and 3rd tab (“Practice Areas”)), general content with navigation that supports nearly unlimited adds to the left nav in terms of content areas.
c. Content page Level 2 (2nd tab (Actual bios of attorney/staff) and 3rd tab (Actual crimes and types of cases my firm handles)), deeper level.
d. Free Case Evaluation page (4th tab) that a potential client can easily fill ou.
e. FAQ Section page (5th tab), that has answers to questions a potential client may have.
f. .Contact Us page (6th tab) that I can easily place a contact us form.
There should also be a link on the homepage to a “Locate Us” page (Link), where I can place our address with Google Maps. This link will not be in the tabs sections up top. Currently, I’m thinking the link with a small icon for a map, will be near the bottom of the home page. Will need template for maps.
Please provide specific portfolio examples of Wordpress templates that you have created. Also note that once the project is complete, all intellectual property rights pertaining to this project will be owned by me.
Legal
- Please see the attached word document.
Also, keep in mind the theme is simple, elegant, smart, and professional.

```html
<!DOCTYPE html>
<html lang="en">
<head>
<meta charset="utf-8">
<title>Harlow Legal</title>
<link href="https://fonts.googleapis.com/css2?family=Arimo:wght@400;700&family=PT+Sans:wght@400;700&display=swap" rel="stylesheet">
<style>
:root{
  --page:#f2f0ea;
  --top-blue:#2d64a8;
  --top-blue-dark:#1c4b8c;
  --brand:#1f3a5c;
  --navy:#1f3a5c;
  --link:#1c4f8f;
  --body-text:#777;
  --rule:#e2e2e2;
  --panel-head-a:#5b86b8;
  --panel-head-b:#2f5d92;
  --white:#fff;
}
*{box-sizing:border-box;margin:0;padding:0}
html,body{width:1200px;height:1072px;overflow:hidden}
body{background:var(--page);font-family:"Arimo",Arial,sans-serif;position:relative}
.top-band{position:absolute;left:0;top:0;width:1200px;height:287px;
  background:linear-gradient(90deg,var(--top-blue-dark),#3f77b9 20%,#4d83c2 50%,#3f77b9 80%,var(--top-blue-dark))}
.page{position:absolute;left:155px;top:9px;width:891px;height:1053px;background:var(--white)}
.header{position:absolute;left:0;top:0;width:891px;height:122px;
  background:linear-gradient(180deg,#fafbfd,#e9eef5)}
.header-photo{position:absolute;left:280px;top:0;width:520px;height:122px;
  background:linear-gradient(90deg,rgba(233,238,245,0),#c7b79a 25%,#8c7a58 45%,#d8cdb8 70%,rgba(233,238,245,0))}
.site-name{position:absolute;left:27px;top:44px;font-family:"PT Sans",sans-serif;font-weight:400;font-size:38px;color:var(--brand);line-height:1}
.lang{position:absolute;right:22px;top:19px;font-family:"PT Sans",sans-serif;font-size:11.5px;color:#444}
.lang a{color:var(--link);text-decoration:none}
.lang .sep{color:#bbb;margin:0 4px}
.search{position:absolute;left:645px;top:81px;width:231px;height:27px;border:1px solid #cfd5de;background:#fff;
  font-size:12.5px;color:#888;padding:6px 10px}
.search svg{position:absolute;right:8px;top:6px}
.nav{position:absolute;left:0;top:122px;width:891px;height:42px;display:flex;
  background:linear-gradient(180deg,#f8f8f8,#ebebeb 55%,#e0e0e0);border-top:1px solid #d6d6d6;border-bottom:3px solid #c3d3e6}
.nav a{display:flex;align-items:center;justify-content:center;font-family:"PT Sans",sans-serif;font-size:13.2px;
  color:var(--navy);text-decoration:none;border-right:1px solid #d2d2d2;height:100%}
.banner{position:absolute;left:10px;top:178px;width:872px;height:287px;
  background:linear-gradient(90deg,#c89a62,#b58556 20%,#d9b27e 40%,#e6c89e 55%,#a8c2de 70%,#8fb0d6 85%,#c2d6ea)}
.sidebar{position:absolute;left:10px;top:475px;width:233px}
.panel{border:1px solid #cfd7e1;background:#fff;margin-bottom:9px}
.panel-head{height:32px;background:linear-gradient(180deg,var(--panel-head-a),var(--panel-head-b));
  color:#fff;font-family:"PT Sans",sans-serif;font-size:16px;padding:6px 8px}
.areas{list-style:none;padding:6px 14px 4px 13px}
.areas li{height:28px;border-bottom:1px dotted #cfcfcf;display:flex;align-items:center;font-size:12.5px;color:var(--link)}
.areas li:last-child{border-bottom:none}
.areas li::before{content:"";border-left:4px solid #bbb;border-top:4px solid transparent;border-bottom:4px solid transparent;margin-right:11px}
.address{padding:13px 14px 0 13px;font-size:11.3px;color:#555;line-height:15px}
.address h3{font-weight:400;font-size:12.7px;color:var(--link);line-height:16px}
.address + .address{border-top:1px dotted #cfcfcf;margin:6px 14px 0 13px;padding:6px 0 0}
.map{margin:8px 2px 2px;height:122px;border:1px solid #ddd;padding:4px}
.map div{width:100%;height:100%;background:linear-gradient(135deg,#e6e3dc,#ddd9cf 40%,#f1e48a 55%,#e3e0d8)}
.main{position:absolute;left:261px;top:475px;width:620px}
.main h1{font-family:"PT Sans",sans-serif;font-weight:400;font-size:25px;color:#555;padding:8px 0 6px;border-bottom:1px solid var(--rule)}
.main h1 span{color:var(--link)}
.main p{font-size:11.25px;line-height:16.9px;color:var(--body-text);margin-top:16px}
.main p:first-of-type{margin-top:12px}
.footer{position:absolute;left:0;top:1015px;width:891px;height:38px;
  background:linear-gradient(180deg,#3d6ea7,#1f4f8a);color:#fff;font-family:"PT Sans",sans-serif;font-size:11.8px;
  display:flex;align-items:center;justify-content:space-between;padding:0 10px}
.footer nav a{color:#fff;text-decoration:none}
.footer nav .sep{margin:0 6px}
</style>
</head>
<body>
<div class="top-band"></div>
<div class="page">
  <header class="header">
    <div class="header-photo" role="img" aria-label="Row of law books on a shelf"></div>
    <div class="site-name">Harlow Legal</div>
    <div class="lang">Select Language: <a href="#">English</a><span class="sep">|</span>Chinese</div>
    <div class="search">Search
      <svg width="14" height="14" viewBox="0 0 14 14"><circle cx="5.5" cy="5.5" r="4" fill="none" stroke="#8aa" stroke-width="1.6"/><line x1="8.5" y1="8.5" x2="13" y2="13" stroke="#8aa" stroke-width="2"/></svg>
    </div>
  </header>
  <nav class="nav">
    <a href="#" style="width:73px">HOME</a>
    <a href="#" style="width:201px">ATTORNEY/STAFF PROFILES</a>
    <a href="#" style="width:134px">PRACTICE AREAS</a>
    <a href="#" style="width:175px">FREE CASE EVALUATION</a>
    <a href="#" style="width:58px">FAQ</a>
    <a href="#" style="width:105px">CONTACT US</a>
  </nav>
  <div class="banner" role="img" aria-label="Scales of justice beside a lawyer reviewing documents"></div>

  <aside class="sidebar">
    <section class="panel">
      <div class="panel-head">Practice Areas</div>
      <ul class="areas">
        <li>Criminal Defense</li><li>Business Law</li><li>Immigration Law</li><li>Personal Injury</li><li>Estate Planning</li>
      </ul>
    </section>
    <section class="panel">
      <div class="panel-head">Locate Us</div>
      <div class="address"><h3>Addresses 1</h3>4120 N . 18 St.Suite 9<br>Lakeview 60412<br>Phone: 555-014-2280<br>Fax: 555-014-2291</div>
      <div class="address"><h3>Addresses 2</h3>4120 N . 18 St.Suite 9<br>Lakeview 60412<br>Phone: 555-014-2280<br>Fax: 555-014-2291</div>
      <div class="map"><div role="img" aria-label="Street map of the office location"></div></div>
    </section>
  </aside>

  <main class="main">
    <h1>Welcome to <span>Harlow Legal</span></h1>
    <p>Lorem ipsum dolor sit amet, consectetur adipisicing elit, sed do eiusmod tempor incididunt ut labore et dolore magna aliqua. Ut enim ad minim veniam, quis nostrud exercitation ullamco laboris nisi ut aliquip ex ea commodo consequat. Duis aute irure dolor in reprehenderit in voluptate velit esse cillum dolore eu fugiat nulla pariatur. Excepteur sint occaecat cupidatat non proident, sunt in culpa qui officia deserunt mollit anim id est laborum. Lorem ipsum dolor sit amet, consectetur adipisicing elit, sed do eiusmod tempor incididunt ut labore et dolore magna aliqua. Ut enim ad minim veniam, quis nostrud exercitation ullamco laboris nisi ut aliquip ex ea commodo consequat. Duis aute irure dolor in reprehenderit in voluptate velit esse cillum dolore eu fugiat nulla pariatur. Excepteur sint occaecat cupidatat non proident, sunt in culpa qui officia deserunt mollit anim id est laborum.</p>
    <p>Lorem ipsum dolor sit amet, consectetur adipisicing elit, sed do eiusmod tempor incididunt ut labore et dolore magna aliqua. Ut enim ad minim veniam, quis nostrud exercitation ullamco laboris nisi ut aliquip ex ea commodo consequat. Duis aute irure dolor in reprehenderit in voluptate velit esse cillum dolore eu fugiat nulla pariatur. Excepteur sint occaecat cupidatat non proident, sunt in culpa qui officia deserunt mollit anim id est laborum.</p>
    <p>Lorem ipsum dolor sit amet, consectetur adipisicing elit, sed do eiusmod tempor incididunt ut labore et dolore magna aliqua. Ut enim ad minim veniam, quis nostrud exercitation ullamco laboris nisi ut aliquip ex ea commodo consequat. Duis aute irure dolor in reprehenderit in voluptate velit esse cillum dolore eu fugiat nulla pariatur. Excepteur sint occaecat cupidatat non proident, sunt in culpa qui officia deserunt mollit anim id est laborum. Lorem ipsum dolor sit amet, consectetur adipisicing elit, sed do eiusmod tempor incididunt ut labore et dolore magna aliqua. Ut enim ad minim veniam, quis nostrud exercitation ullamco laboris nisi ut aliquip ex ea commodo consequat.</p>
    <p>Lorem ipsum dolor sit amet, consectetur adipisicing elit, sed do eiusmod tempor incididunt ut labore et dolore magna aliqua. Ut enim ad minim veniam, quis nostrud exercitation ullamco laboris nisi ut aliquip ex ea commodo consequat. Duis aute irure dolor in reprehenderit in voluptate velit esse cillum dolore eu fugiat nulla pariatur. Excepteur sint occaecat cupidatat non proident, sunt in culpa qui officia deserunt mollit anim id est laborum. Lorem ipsum dolor sit amet, consectetur adipisicing elit, sed do eiusmod tempor incididunt ut labore et dolore magna aliqua. Ut enim ad minim veniam, quis nostrud exercitation ullamco laboris nisi ut aliquip ex ea commodo consequat.</p>
  </main>

  <footer class="footer">
    <span>Copyright © 2011 Harlow Legal. all rights reserved</span>
    <nav><a href="#">Home</a><span class="sep">|</span><a href="#">Attorney/Staff Profiles</a><span class="sep">|</span><a href="#">Practice Areas</a><span class="sep">|</span><a href="#">Free Case Evaluation</a><span class="sep">|</span><a href="#">FAQ</a><span class="sep">|</span><a href="#">Contact Us</a></nav>
  </footer>
</div>
</body>
</html>
```